I need creative and unique business card design using my company logo. Ok to change logo color. We are a small brokerage doing both Real Estate and Mortgage services. Need to have the follow on business card;
1. agent name - Mila Fenton - Realtor
2. cell - 949-555-0182
3. license number - DRE 04917362
4. business name - Brightway Estates & Lending, Inc
5. business office - 626-555-0147
6. business address - 287 W. Larkmoor Ave #214, Arcadia CA 91088
7. business logo - attached (ok to use different color on logo)

```html
<!DOCTYPE html>
<html lang="en">
<head>
<meta charset="utf-8">
<title>Brightway Estates &amp; Lending – Business Card</title>
<link rel="stylesheet" href="https://fonts.googleapis.com/css2?family=Montserrat:wght@400;500;700&display=swap">
<style>
  :root {
    --backdrop: #1c1c1c;
    --blue-deep: #2a5cad;
    --blue-mid: #3a7cc6;
    --blue-light: #4c9fda;
    --white: #ffffff;
    --card-shadow: rgba(0,0,0,0.55);
  }
  * { box-sizing: border-box; margin: 0; padding: 0; }
  html, body {
    width: 1200px; height: 1015px; overflow: hidden;
    background: var(--backdrop);
    font-family: "Montserrat", sans-serif;
  }
  .canvas { position: relative; width: 1200px; height: 1015px; }

  .card {
    position: absolute;
    width: 700px; height: 400px;
    box-shadow: 0 18px 40px var(--card-shadow);
    overflow: hidden;
  }
  .card--front {
    left: 70px; top: 80px;
    background: linear-gradient(180deg, var(--blue-mid) 0%, var(--blue-light) 45%, var(--blue-deep) 100%);
  }
  .card--back {
    left: 430px; top: 535px;
    background: var(--white);
    display: flex;
  }

  .brand {
    display: flex; flex-direction: column; align-items: center; gap: 22px;
    text-align: center;
  }
  .card--front .brand {
    position: absolute; inset: 0; justify-content: center;
    color: var(--white);
  }
  .brand__mark { width: 64px; height: 64px; border-radius: 50%; background: currentColor; }
  .brand__name {
    font-weight: 500; font-size: 26px; letter-spacing: 6px; text-transform: uppercase;
    line-height: 1.35;
  }

  .back__info {
    position: relative;
    width: 390px; height: 100%;
    background: linear-gradient(180deg, var(--blue-mid) 0%, var(--blue-light) 50%, var(--blue-deep) 100%);
    color: var(--white);
    padding: 46px 0 0 42px;
  }
  .back__divider {
    width: 14px; height: 100%;
    background: linear-gradient(90deg, var(--white) 0 4px, var(--blue-deep) 4px 9px, var(--white) 9px);
  }
  .back__brand {
    flex: 1; display: flex; align-items: center; justify-content: center;
    color: var(--blue-deep);
  }
  .back__brand .brand__name { font-size: 19px; letter-spacing: 4px; }
  .back__brand .brand__mark { width: 52px; height: 52px; background: var(--blue-mid); }

  .agent__name { font-weight: 700; font-size: 25px; text-transform: uppercase; line-height: 1.05; }
  .agent__role { font-size: 17px; margin-bottom: 10px; }
  .contact-line { display: flex; align-items: center; gap: 6px; font-size: 17px; line-height: 1.35; }
  .contact-line svg { width: 16px; height: 18px; flex: none; }
  .agent__license { font-size: 17px; padding-left: 22px; }

  .office { position: absolute; left: 42px; bottom: 40px; font-size: 16px; line-height: 1.35; }
  .office__name { font-weight: 700; }
  .office .contact-line { margin-top: 10px; }
</style>
</head>
<body>
<main class="canvas">
  <section class="card card--front" aria-label="Card front">
    <div class="brand">
      <span class="brand__mark"></span>
      <p class="brand__name">Brightway Estates<br>&amp; Lending, Inc</p>
    </div>
  </section>

  <section class="card card--back" aria-label="Card back">
    <div class="back__info">
      <h1 class="agent__name">Mila Fenton</h1>
      <p class="agent__role">Realtor</p>
      <p class="contact-line">
        <svg viewBox="0 0 16 20" fill="none" stroke="currentColor" stroke-width="1.6"><rect x="2" y="1" width="12" height="18" rx="2"/><line x1="6" y1="16" x2="10" y2="16"/></svg>
        949-555-0182
      </p>
      <p class="agent__license">LIC DRE 04917362</p>

      <address class="office" style="font-style:normal">
        <p class="office__name">Brightway Estates &amp; Lending, Inc</p>
        <p>287 W. Larkmoor Ave #214,</p>
        <p>Arcadia CA 91088</p>
        <p class="contact-line">
          <svg viewBox="0 0 20 20" fill="currentColor"><path d="M4 2l3 0 1.5 4-2 1.5a11 11 0 0 0 6 6l1.5-2 4 1.5v3a2 2 0 0 1-2 2A16 16 0 0 1 2 4a2 2 0 0 1 2-2z"/></svg>
          626-555-0147
        </p>
      </address>
    </div>
    <div class="back__divider"></div>
    <div class="back__brand">
      <div class="brand">
        <span class="brand__mark"></span>
        <p class="brand__name">Brightway Estates<br>&amp; Lending, Inc</p>
      </div>
    </div>
  </section>
</main>
</body>
</html>
```